redesing professional certificate

Redesign our certificate to more a professional look and to make it look like a-wanna have - Best in adobe photoshop, because this template will be our basic, and we have in our education different levels, basic, upper, lower, complex, master level. I usually add a small picture to show what level they are. Or when you have a better suggestion I a gladly to hear.
We teach to physiotherapist so it has to look professional.

Target Market(s)

physiotherapist

Industry/Entity Type

Health Care

Requirements
Must have
• our logo

```html
<!DOCTYPE html>
<html lang="en">
<head>
<meta charset="utf-8">
<title>Certificate – Myofascial Balance Method</title>
<link rel="stylesheet" href="https://fonts.googleapis.com/css2?family=Montserrat:ital,wght@0,400;0,500;0,700;1,500;1,700&display=swap">
<style>
  :root {
    --navy: #1c3a57;
    --ink: #1e3550;
    --dot-blue: #1d5fa6;
    --paper: #ffffff;
  }
  * { margin: 0; padding: 0; box-sizing: border-box; }
  html, body { width: 848px; height: 1200px; overflow: hidden; background: var(--paper); }
  body { font-family: "Montserrat", sans-serif; color: var(--ink); }

  .certificate { position: relative; width: 848px; height: 1200px; overflow: hidden; background: var(--paper); }

  .wave-decoration {
    position: absolute; right: 0; top: 0; width: 420px; height: 1200px;
    background:
      radial-gradient(ellipse 160px 420px at 100% 35%, rgba(29,95,166,0.28), rgba(29,95,166,0) 70%),
      radial-gradient(ellipse 220px 260px at 95% 95%, rgba(29,95,166,0.32), rgba(29,95,166,0) 70%),
      radial-gradient(ellipse 260px 500px at 80% 60%, rgba(29,95,166,0.10), rgba(29,95,166,0) 75%);
  }

  .brand {
    position: absolute; right: 16px; top: 66px;
    display: flex; align-items: center; gap: 10px;
    width: 200px; flex-direction: column;
  }
  .brand-circle { width: 96px; height: 96px; border-radius: 50%; background: var(--navy); }
  .brand-name {
    font-weight: 700; font-size: 15px; line-height: 1.25; text-align: center;
    color: var(--navy); letter-spacing: 0.02em;
  }

  .title {
    position: absolute; left: 58px; top: 70px;
    font-size: 50px; font-weight: 700; color: var(--navy); letter-spacing: -0.5px;
  }

  .recipient {
    position: absolute; left: 70px; top: 322px;
    font-size: 27px; font-weight: 700; font-style: italic; color: var(--navy);
  }
  .course-details {
    position: absolute; left: 70px; top: 362px;
    font-size: 21px; font-weight: 500; line-height: 27px; color: var(--ink);
  }

  .signatory { position: absolute; top: 708px; }
  .signatory.first { left: 70px; }
  .signatory.second { left: 375px; }
  .signatory-name { font-size: 25px; font-weight: 700; font-style: italic; color: var(--navy); line-height: 1.1; }
  .signatory-role { font-size: 17px; font-weight: 700; font-style: italic; color: var(--navy); margin-top: 2px; }

  .registration {
    position: absolute; left: 70px; top: 798px;
    font-size: 18px; font-weight: 500;
  }
  .registration em { font-weight: 700; }

  .maintenance-note {
    position: absolute; left: 68px; top: 858px; width: 560px;
    font-size: 18px; font-weight: 500; line-height: 24px;
  }

  .issuer-address {
    position: absolute; left: 72px; top: 969px;
    font-size: 18px; font-weight: 500; line-height: 24px;
  }

  .tagline {
    position: absolute; left: 72px; top: 1112px;
    font-size: 18px; font-weight: 500;
  }
</style>
</head>
<body>
  <main class="certificate">
    <div class="wave-decoration" role="img" aria-label="Flowing wave pattern of fine blue dots along the right edge"></div>

    <div class="brand">
      <div class="brand-circle"></div>
      <div class="brand-name">Myofascial Balance Method</div>
    </div>

    <h1 class="title">Certificate</h1>

    <p class="recipient">Lucas Moreno</p>
    <p class="course-details">
      has completed the fasciatherapy level 1 course<br>
      - 3 days, 75-77 february 2020<br>
      Kópavogur, Iceland 77 february 2020.
    </p>

    <div class="signatory first">
      <p class="signatory-name">vlr. HT Brandsma</p>
      <p class="signatory-role">Co-Director</p>
    </div>
    <div class="signatory second">
      <p class="signatory-name">vlr. RK Osei</p>
      <p class="signatory-role">Co-Director</p>
    </div>

    <p class="registration">Registration number: <em>7 ICE 20</em></p>

    <p class="maintenance-note">
      The Myofascial Balance Method ongoing certification is contingent upon meeting the requirements of the maintenance of the certification of Fasciatherapy
    </p>

    <address class="issuer-address" style="font-style: normal;">
      Tissuelink BV Derde<br>
      Lindenhofstraat 14<br>
      1032KM Amsterdam The<br>
      Netherlands
    </address>

    <p class="tagline">Specialists in fasciatherapy innovation</p>
  </main>
</body>
</html>
```